Gentleman's grooming products require a business card

I need a business card that incorporates the logo [ or parts of ] that we had Pixel Hive design for us as uploaded.

We sell online, mens grooming products including moustache waxes, beard oils and shaving accessories.
We want a card that is classy, professional and a card that shouts mens products.

Target Market(s)

Young professional male market

Industry/Entity Type

Business

Contact Information for Business Card

Ross and Edith Carwell
Lather and Lore
Purveyors of gentleman's stiffeners and grooming requisites
M :0418529647
E : ross@latherandlore.com.au
E : edith@latherandlore.com.au
E : sales@theblokesbalmery.com.au

W : www.latherandlore.com.au

Requirements
Must have
• Class
Nice to have
• Professionalism

```html
<!DOCTYPE html>
<html lang="en">
<head>
<meta charset="utf-8">
<title>Lather and Lore — Business Card</title>
<link rel="stylesheet" href="https://fonts.googleapis.com/css2?family=Open+Sans:wght@400;600&display=swap">
<style>
  :root {
    --stage: #d6d6d6;
    --card-black: #050505;
    --card-gold: #f6b524;
    --ink-white: #ffffff;
    --art-light: #e8e8e8;
    --art-dark: #8a8a8a;
  }
  * { box-sizing: border-box; margin: 0; padding: 0; }
  html, body { width: 1200px; height: 800px; overflow: hidden; }
  body {
    background: var(--stage);
    font-family: "Open Sans", sans-serif;
    display: flex;
    align-items: center;
    justify-content: center;
    gap: 60px;
  }
  .card {
    width: 460px;
    height: 460px;
    position: relative;
    color: var(--ink-white);
    box-shadow: 0 6px 18px rgba(0,0,0,0.18);
  }
  .card--front { background: var(--card-black); }
  .card--back { background: var(--card-gold); padding: 90px 0 0 52px; }

  .brand-name {
    position: absolute;
    top: 58px;
    left: 44px;
    font-size: 40px;
    font-weight: 400;
    letter-spacing: 0.5px;
    color: var(--ink-white);
  }
  .brand-art {
    position: absolute;
    top: 128px;
    left: 150px;
    width: 250px;
    height: 290px;
    border-radius: 6px;
    background: linear-gradient(160deg, var(--art-light), var(--art-dark));
  }

  .holder-name { font-size: 27px; font-weight: 600; line-height: 1.2; }
  .tagline { font-size: 16px; font-weight: 400; line-height: 1.3; margin: 6px 0 0 30px; }
  .contact-list { list-style: none; margin-top: 44px; }
  .contact-item {
    display: flex;
    align-items: center;
    gap: 9px;
    font-size: 16px;
    line-height: 1.55;
  }
  .contact-item--web { margin-top: 22px; }
  .contact-icon { width: 15px; height: 15px; flex: none; fill: var(--ink-white); }
</style>
</head>
<body>
  <section class="card card--front" aria-label="Card front">
    <div class="brand-name">Lather and Lore</div>
    <div class="brand-art" role="img" aria-label="Illustration of a moustached gentleman with crossed barber scissors"></div>
  </section>

  <section class="card card--back" aria-label="Card back">
    <h1 class="holder-name">Ross and Edith Carwell</h1>
    <p class="tagline">Purveyors of gentleman's stiffeners<br>and grooming requisites</p>
    <ul class="contact-list">
      <li class="contact-item">
        <svg class="contact-icon" viewBox="0 0 16 16"><path d="M3.6 1.2l2.3 2.6-1.4 1.9c.9 2 2.6 3.8 4.6 4.7l1.9-1.4 2.6 2.3-1.3 2.6C6.6 13.6 2.3 9.3 1 3.6z"/></svg>
        <span>0418529647</span>
      </li>
      <li class="contact-item">
        <svg class="contact-icon" viewBox="0 0 16 16"><path d="M1 3h14v10H1z M2.5 4.5v.3L8 8.9l5.5-4.1v-.3z"/></svg>
        <span>ross@latherandlore.com.au</span>
      </li>
      <li class="contact-item">
        <svg class="contact-icon" viewBox="0 0 16 16"><path d="M1 3h14v10H1z M2.5 4.5v.3L8 8.9l5.5-4.1v-.3z"/></svg>
        <span>edith@latherandlore.com.au</span>
      </li>
      <li class="contact-item">
        <svg class="contact-icon" viewBox="0 0 16 16"><path d="M1 3h14v10H1z M2.5 4.5v.3L8 8.9l5.5-4.1v-.3z"/></svg>
        <span>sales@theblokesbalmery.com.au</span>
      </li>
      <li class="contact-item contact-item--web">
        <svg class="contact-icon" viewBox="0 0 16 16"><circle cx="8" cy="8" r="7"/><path d="M1.5 8h13M8 1.2c-2.4 2-2.4 11.6 0 13.6M8 1.2c2.4 2 2.4 11.6 0 13.6" stroke="#f6b524" stroke-width="1" fill="none"/></svg>
        <span>www.latherandlore.com.au</span>
      </li>
    </ul>
  </section>
</body>
</html>
```